Good Friday Graphic - 7 Last Sayings of Christ

I need a graphic created with the number 7 big, bold and stands out more than anything else with the line Seven Last Sayings of Christ.
I need the pictures of the attached preachers in the graphic in this order:
Word 1 – Dr. Marla Quincey, Bright Harbor Christian Church
Word 2 – Dr. Owen Brickell, Fernhollow Baptist Church
Word 3 – Pastor Lyle Dunmore, Wexley Avenue Baptist Church
Word 4 – Dr. Jonathan Pruitt, Mount Calder Baptist Church
Word 5 – Bishop Harold Winslowe, Silver Crest Cathedral
Word 6 – Dr. Milton Archer, Briarwood Fellowship Baptist Church
Word 7 – Dr. Louis T. Hale, Cedar Bend Baptist Church, Lakeside
Date: Good Friday, April 14, 2017
Time: 12 Noon
Location:
Mount Calder Baptist Church
3871 West Lindell Road
Memphis, TN 38492
I need the graphic in the following sizes:
1500x600
960x720
820x312

```html
<!DOCTYPE html>
<html lang="en">
<head>
<meta charset="utf-8">
<title>Seven Last Sayings of Christ – Good Friday</title>
<link rel="stylesheet" href="https://fonts.googleapis.com/css2?family=Bungee&family=Russo+One&family=Roboto+Condensed:wght@400;700&display=swap">
<style>
  :root{
    --sky-top:#c9572a;
    --sky-mid:#e98a3a;
    --sky-glow:#f7c56a;
    --ground:#3a1e12;
    --ink:#111111;
    --white:#ffffff;
    --yellow:#ffe600;
    --gold:#ffcc1a;
    --cross-sky-a:#7f8a92;
    --cross-sky-b:#c98a4a;
  }
  *{margin:0;padding:0;box-sizing:border-box}
  html,body{width:1200px;height:488px;overflow:hidden;background:#fff}
  .banner{position:relative;width:1200px;height:488px;overflow:hidden;font-family:"Roboto Condensed",sans-serif;color:var(--white)}
  .backdrop{position:absolute;inset:0;
    background:
      radial-gradient(ellipse 520px 240px at 52% 78%, var(--sky-glow) 0%, rgba(247,197,106,0) 70%),
      linear-gradient(180deg,var(--sky-top) 0%,var(--sky-mid) 45%,#d9773a 72%,var(--ground) 100%);}
  .backdrop-figure{position:absolute;left:0;top:230px;width:240px;height:258px;
    background:linear-gradient(180deg,rgba(40,20,10,0) 0%,rgba(40,20,10,.55) 55%,rgba(30,14,8,.85) 100%)}
  .seven{position:absolute;left:0;top:0;width:480px;height:488px}
  .headline{position:absolute;left:476px;top:40px;display:flex;align-items:baseline;gap:12px;white-space:nowrap;font-weight:400}
  .headline .last{font-family:"Bungee",sans-serif;font-size:52px;line-height:1;color:var(--white)}
  .headline .middle{font-family:"Bungee",sans-serif;font-size:27px;line-height:1;color:var(--white)}
  .headline .christ{font-family:"Bungee",sans-serif;font-size:52px;line-height:1;color:var(--yellow)}
  .event-when{position:absolute;left:478px;top:110px;font-size:20px;color:var(--white);white-space:nowrap}
  .event-when b{color:var(--yellow);font-weight:400}
  .event-when .time{margin-left:30px}
  .speaker{position:absolute;display:flex;gap:10px;align-items:flex-start}
  .portrait{flex:none;width:66px;height:66px;border:3px solid var(--white);
    background:linear-gradient(160deg,#6b4a38 0%,#2e1f18 100%);box-shadow:0 2px 6px rgba(0,0,0,.35)}
  .word{font-family:"Russo One",sans-serif;font-size:25px;line-height:1;color:var(--white);white-space:nowrap}
  .name{font-size:15px;font-weight:700;color:var(--white);margin-top:10px;white-space:nowrap;line-height:1.1}
  .church{font-size:9px;color:var(--white);margin-top:2px;white-space:nowrap}
  .location{position:absolute;right:62px;top:276px;text-align:right;font-size:15px;font-weight:700;line-height:1.3;font-style:normal}
  .location .label{color:var(--gold)}
  .book-now{position:absolute;left:944px;top:381px;width:196px;height:46px;border-radius:8px;
    background:linear-gradient(180deg,#fff45a,var(--yellow));border:2px solid #c9a800;
    display:flex;align-items:center;justify-content:space-between;padding:0 7px 0 16px;white-space:nowrap;
    font-family:"Roboto Condensed",sans-serif;font-weight:700;font-size:23px;color:var(--ink);box-shadow:0 3px 6px rgba(0,0,0,.35)}
  .book-now svg{flex:none;width:32px;height:32px}
</style>
</head>
<body>
<div class="banner">
  <div class="backdrop" role="img" aria-label="Sunset sky over a hillside"></div>
  <div class="backdrop-figure" role="img" aria-label="Silhouette of a kneeling person in prayer"></div>

  <svg class="seven" viewBox="0 0 480 488" role="img" aria-label="Large number seven framing a wooden cross against the sky">
    <defs>
      <linearGradient id="seven-fill" x1="0" y1="0" x2="0.4" y2="1">
        <stop offset="0" stop-color="var(--cross-sky-a)"/>
        <stop offset="1" stop-color="var(--cross-sky-b)"/>
      </linearGradient>
    </defs>
    <path d="M184 50 H450 V140 L392 474 H298 L346 156 H184 Z" fill="url(#seven-fill)" stroke="var(--ink)" stroke-width="9" stroke-linejoin="round"/>
  </svg>

  <h1 class="headline"><span class="last">LAST</span><span class="middle">sayings of</span><span class="christ">CHRIST</span></h1>
  <p class="event-when">Good Friday: <b>April 14, 2017</b><span class="time">Time:<b>12 Noon</b></span></p>

  <div class="speaker" style="left:470px;top:180px">
    <div class="portrait" role="img" aria-label="Portrait of Dr. Marla Quincey"></div>
    <div><div class="word">WORD 1</div><div class="name">Dr. Marla Quincey</div><div class="church">Bright Harbor Christian Church</div></div>
  </div>
  <div class="speaker" style="left:717px;top:180px">
    <div class="portrait" role="img" aria-label="Portrait of Dr. Owen Brickell"></div>
    <div><div class="word">WORD 2</div><div class="name">Dr. Owen Brickell</div><div class="church">Fernhollow Baptist Church</div></div>
  </div>
  <div class="speaker" style="left:920px;top:180px">
    <div class="portrait" role="img" aria-label="Portrait of Pastor Lyle Dunmore"></div>
    <div><div class="word">WORD 3</div><div class="name">Pastor Lyle Dunmore</div><div class="church">Wexley Avenue Baptist Church</div></div>
  </div>
  <div class="speaker" style="left:423px;top:269px">
    <div class="portrait" role="img" aria-label="Portrait of Dr. Jonathan Pruitt"></div>
    <div><div class="word">WORD 4</div><div class="name">Dr. Jonathan Pruitt</div><div class="church">Mount Calder Baptist Church</div></div>
  </div>
  <div class="speaker" style="left:669px;top:269px">
    <div class="portrait" role="img" aria-label="Portrait of Bishop Harold Winslowe"></div>
    <div><div class="word">WORD 5</div><div class="name">Bishop Harold Winslowe</div><div class="church">Silver Crest Cathedral</div></div>
  </div>
  <div class="speaker" style="left:376px;top:359px">
    <div class="portrait" role="img" aria-label="Portrait of Dr. Milton Archer"></div>
    <div><div class="word">WORD 6</div><div class="name">Dr. Milton Archer</div><div class="church">Briarwood Fellowship Baptist Church</div></div>
  </div>
  <div class="speaker" style="left:622px;top:359px">
    <div class="portrait" role="img" aria-label="Portrait of Dr. Louis T. Hale"></div>
    <div><div class="word">WORD 7</div><div class="name">Dr. Louis T. Hale</div><div class="church">Cedar Bend Baptist Church, Lakeside</div></div>
  </div>

  <address class="location">
    <div class="label">Location:</div>
    <div>Mount Calder Baptist Church,</div>
    <div>3871 West Lindell Road</div>
    <div>Memphis, TN 38492</div>
  </address>

  <div class="book-now"><span>BOOK NOW!</span>
    <svg viewBox="0 0 34 34" aria-hidden="true"><circle cx="17" cy="17" r="16" fill="#111"/><path d="M13 9 L23 17 L13 25 Z" fill="#ffe600"/></svg>
  </div>
</div>
</body>
</html>
```